Create a Dynamic, Connecting, Professional looking PowerPoint Design master for our company.

Power point design

Target Market: High worth individuals and corporate group
Industry: Sport and services

Landscape format

Should include various slide such as:
Introduction page (photo background- inclusive logo)
Company presentation (with photos of various projects)
Different slide layouts to place general information with large photo & logo (in different sizes) as well as standard elements, such as text boxes, lines, default shapes, etc
Timeline page
Table pages
Various infographic style pages with editable chart
Our service page – Icons
Location page (world map)
Comparaison pages (3 offers to compare)
Closing page – thank you & contact
Page numbering

Colors:
#6ea6fa
#517ed8
#3758b4
#203390
#060d6c
#2EC193
White / Grey and black

Fonts:
Work sans / Helveticanow / Or other suitable.
Creative use of the logo in the slides. The Timrel icon may be used as a small device or large watermark to enhance branding.

The uploaded photos are indicative of the ones that we would like to use (ie: sail racing) there are here for you to include in the design but would need to be easily replaceable by the final photos we would be using.

If you have any questions or need any aditional material, please send me a message and I will try to respond to it as quickly as possible (bearing in mind that my time zone is UTC +2)

Target Market(s)

High worth individuals and corporate groups

Industry/Entity Type

Sport and services (sailing)

Font styles to use
Other font styles liked:
• Work Sans / Helveticanow

Colors
0054AA
0677BA
7BADD7
CADEEF
E8F1F8
00AB8E
00BBA5
67D7C9
C6EFE9
E9F9F6

Requirements
Must have
• Introduction page (photo background- inclusive logo) Company presentation (with photos of various projects) Different slide layouts to place general information with large photo & logo (in different sizes) as well as standard elements, such as text boxes, lines, default shapes, etc Timeline page Table pages Various infographic style pages with editable chart Our service page – Icons Location page (world map) Comparaison pages (3 offers to compare) Closing page – thank you & contact Page numbering
Nice to have
• Creative use of the logo in the slides. The Timrel icon may be used as a small device or large watermark to enhance branding.

```html
<!DOCTYPE html>
<html lang="en">
<head>
<meta charset="utf-8">
<title>Timrel Presentation Master</title>
<link rel="stylesheet" href="https://fonts.googleapis.com/css2?family=Work+Sans:wght@300;400;500;600;700&display=swap">
<style>
:root{
  --sky:#6ea6fa;
  --mid:#517ed8;
  --blue:#3758b4;
  --navy:#203390;
  --deep:#060d6c;
  --grey:#8a8f9c;
  --ink:#1a1f3a;
  --white:#ffffff;
}
*{box-sizing:border-box;margin:0;padding:0}
html,body{width:1200px;height:2351px;overflow:hidden}
body{font-family:"Work Sans",Arial,sans-serif;background:#ffffff;position:relative;color:var(--ink)}
.stage{position:absolute;left:0;top:0;width:1200px;height:710px;background:#eef0f4}
.brand{position:absolute;display:flex;align-items:center;gap:4px;font-weight:700;color:var(--deep);letter-spacing:.02em;line-height:1}
.brand .dot{border-radius:50%;background:var(--deep);display:block}
.brand.light{color:#fff}
.brand.light .dot{background:#fff}
.slide{position:absolute;width:374px;height:211px;background:#fff;overflow:hidden;box-shadow:0 0 0 1px #e3e6ee}
.photo{position:absolute;background:
  radial-gradient(ellipse 60% 40% at 30% 60%,rgba(255,255,255,.10),rgba(255,255,255,0) 70%),
  linear-gradient(180deg,#6f93c9 0%,#3a6cb8 10%,#1f58aa 35%,#154993 65%,#0c336f 100%)}
.photo.crew{background:
  radial-gradient(ellipse 45% 60% at 25% 55%,rgba(255,255,255,.55),rgba(255,255,255,0) 70%),
  linear-gradient(115deg,#eef0f4 0%,#c7cfdb 28%,#8194b3 52%,#3a66ad 76%,#1c4c99 100%)}
.photo.fleet{background:
  radial-gradient(ellipse 70% 40% at 50% 25%,rgba(255,255,255,.45),rgba(255,255,255,0) 70%),
  linear-gradient(180deg,#dadde1 0%,#bcc1c7 35%,#9ea4ac 70%,#7e858e 100%)}
.photo.race{background:
  radial-gradient(ellipse 40% 50% at 60% 45%,rgba(214,64,64,.18),rgba(214,64,64,0) 70%),
  linear-gradient(180deg,#eef1f5 0%,#d5dbe3 35%,#a9b4c2 62%,#6a7c93 84%,#3e5068 100%)}
.photo.foil{background:
  radial-gradient(ellipse 50% 30% at 45% 70%,rgba(255,255,255,.35),rgba(255,255,255,0) 70%),
  linear-gradient(180deg,#cdd3dc 0%,#8e9bac 34%,#415568 58%,#253746 100%)}
.photo.green{background:
  radial-gradient(ellipse 45% 25% at 55% 72%,rgba(140,198,63,.85),rgba(140,198,63,0) 70%),
  linear-gradient(160deg,#6a7b89 0%,#45596a 45%,#33475a 75%,#263846 100%)}
.photo.tint{background:
  radial-gradient(ellipse 40% 70% at 55% 40%,rgba(255,255,255,.10),rgba(255,255,255,0) 70%),
  linear-gradient(160deg,#2a3d9e,#1c2d86)}
.photo.bluetint{background:
  radial-gradient(ellipse 50% 70% at 60% 50%,rgba(255,255,255,.12),rgba(255,255,255,0) 70%),
  linear-gradient(170deg,#5a8de3,#3d70cf)}
.photo.map{background:
  radial-gradient(ellipse 22% 30% at 20% 35%,rgba(32,51,144,.55),rgba(32,51,144,0) 75%),
  radial-gradient(ellipse 12% 22% at 33% 72%,rgba(32,51,144,.5),rgba(32,51,144,0) 75%),
  radial-gradient(ellipse 30% 28% at 68% 38%,rgba(120,128,140,.55),rgba(120,128,140,0) 75%),
  radial-gradient(ellipse 14% 22% at 52% 62%,rgba(120,128,140,.5),rgba(120,128,140,0) 75%),
  radial-gradient(ellipse 12% 12% at 84% 78%,rgba(120,128,140,.5),rgba(120,128,140,0) 75%),
  #ffffff}
.band{position:absolute;left:0;width:100%;background:var(--sky)}
.bracket{position:absolute;width:14px;height:14px;border:3px solid var(--navy)}
.bracket.tl{border-right:none;border-bottom:none}
.bracket.br{border-left:none;border-top:none}
.bracket.tr{border-left:none;border-bottom:none}
.bracket.sky{border-color:var(--sky)}
.titlebox{position:absolute;background:var(--navy);color:#fff;text-align:center;display:flex;flex-direction:column;align-items:center;justify-content:center}
.titlebox h1{font-weight:400;line-height:1.1}
.titlebox .rule{background:var(--sky);margin:6px 0}
.titlebox .date{border:1px solid var(--sky);color:#cfe0ff}
.copy{position:absolute;color:#fff;font-size:4px;font-weight:600}
.heading{position:absolute;font-weight:700;color:var(--navy);line-height:1.05;font-size:12px}
.heading span{color:var(--sky)}
.body{position:absolute;font-size:4.2px;line-height:1.3;color:#444a5c}
.pg{position:absolute;right:8px;bottom:8px;width:7px;height:7px;border-radius:50%;background:var(--sky);color:#fff;font-size:3.5px;display:flex;align-items:center;justify-content:center}
.foot{left:10px;bottom:8px;font-size:8px}
.foot .dot{width:6px;height:6px}
.stitle{position:absolute;left:0;width:100%;text-align:center;font-weight:600;color:var(--navy);font-size:11.5px}
.card{position:absolute;background:var(--sky);border-radius:3px;overflow:hidden;color:#fff;text-align:center}
.card .photo{position:relative;display:block;height:66px}
.card p{font-size:4.2px;line-height:1.3;padding:3px 6px 0}
.icon{display:block}
table{border-collapse:collapse;width:100%}
</style>
</head>
<body>

<div class="stage"></div>
<div class="brand" style="right:78px;top:72px;font-size:32px"><i class="dot" style="width:22px;height:22px"></i>TIMREL</div>

<!-- Hero cover -->
<div class="slide" style="left:250px;top:150px;width:620px;height:349px">
  <div class="brand" style="left:26px;top:26px;font-size:22px"><i class="dot" style="width:14px;height:14px"></i>TIMREL</div>
  <div class="photo" role="img" aria-label="Racing sailboats on open deep-blue sea" style="left:0;top:75px;width:620px;height:200px"></div>
  <div class="band" style="top:275px;height:74px"></div>
  <div class="copy" style="left:40px;top:305px;font-size:7px;font-weight:500">Copyright © 2022 TIMREL. All rights reserved.</div>
  <div class="bracket tl" style="left:232px;top:45px;width:24px;height:24px;border-width:5px"></div>
  <div class="titlebox" style="left:277px;top:45px;width:256px;height:256px">
    <h1 style="font-size:21px">PRESENTATION<br>Title Goes Here</h1>
    <div class="rule" style="width:22px;height:2px;margin:12px 0"></div>
    <p style="font-size:9px;line-height:1.35">Lorem ipsum dolor sit amet,<br>consectetur adipiscing elit.</p>
    <div class="date" style="font-size:6px;padding:4px 20px;margin-top:16px">November 15, 2022</div>
  </div>
  <div class="bracket br" style="left:533px;top:277px;width:24px;height:24px;border-width:5px"></div>
</div>

<!-- Row 1 : covers -->
<div class="slide" style="left:20px;top:733px">
  <div class="brand" style="left:14px;top:12px;font-size:13px"><i class="dot" style="width:9px;height:9px"></i>TIMREL</div>
  <div class="photo" role="img" aria-label="Racing sailboats on deep-blue sea" style="left:0;top:45px;width:374px;height:120px"></div>
  <div class="band" style="top:165px;height:46px"></div>
  <div class="copy" style="left:22px;top:188px">Copyright © 2022 TIMREL. All rights reserved.</div>
  <div class="bracket tl" style="left:142px;top:28px"></div>
  <div class="titlebox" style="left:167px;top:28px;width:155px;height:155px">
    <h1 style="font-size:14px">PRESENTATION<br>Title Goes Here</h1>
    <div class="rule" style="width:14px;height:1px"></div>
    <p style="font-size:6px;line-height:1.3">Lorem ipsum dolor sit amet,<br>consectetur adipiscing elit.</p>
    <div class="date" style="font-size:3.5px;padding:2px 12px;margin-top:10px">November 15, 2022</div>
  </div>
  <div class="bracket br" style="left:322px;top:183px"></div>
</div>

<div class="slide" style="left:413px;top:733px">
  <div class="brand" style="left:14px;top:12px;font-size:13px"><i class="dot" style="width:9px;height:9px"></i>TIMREL</div>
  <div class="photo crew" role="img" aria-label="Crew working winches on deck of a racing yacht" style="left:0;top:45px;width:374px;height:120px"></div>
  <div class="band" style="top:165px;height:46px"></div>
  <div class="copy" style="left:22px;top:188px">Copyright © 2022 TIMREL. All rights reserved.</div>
  <div class="bracket tl" style="left:142px;top:28px"></div>
  <div class="titlebox" style="left:167px;top:28px;width:155px;height:155px;background:rgba(32,51,144,.92)">
    <h1 style="font-size:14px">PRESENTATION<br>Title Goes Here</h1>
    <div class="rule" style="width:14px;height:1px"></div>
    <p style="font-size:6px;line-height:1.3">Lorem ipsum dolor sit amet,<br>consectetur adipiscing elit.</p>
    <div class="date" style="font-size:3.5px;padding:2px 12px;margin-top:10px">November 15, 2022</div>
  </div>
  <div class="bracket br" style="left:322px;top:183px"></div>
</div>

<div class="slide" style="left:806px;top:733px">
  <div class="brand" style="left:14px;top:12px;font-size:13px"><i class="dot" style="width:9px;height:9px"></i>TIMREL</div>
  <div class="photo" role="img" aria-label="Racing sailboats on deep-blue sea" style="left:0;top:45px;width:374px;height:120px"></div>
  <div class="band" style="top:165px;height:46px"></div>
  <div class="copy" style="left:22px;top:188px">Copyright © 2022 TIMREL. All rights reserved.</div>
  <div class="bracket tl" style="left:142px;top:28px"></div>
  <div class="titlebox" style="left:167px;top:0;width:155px;height:183px;padding-top:28px">
    <h1 style="font-size:14px">PRESENTATION<br>Title Goes Here</h1>
    <div class="rule" style="width:14px;height:1px"></div>
    <p style="font-size:6px;line-height:1.3">Lorem ipsum dolor sit amet,<br>consectetur adipiscing elit.</p>
    <div class="date" style="font-size:3.5px;padding:2px 12px;margin-top:10px">November 15, 2022</div>
  </div>
  <div class="bracket br" style="left:322px;top:183px"></div>
</div>

<!-- Row 2 -->
<div class="slide" style="left:20px;top:963px">
  <div class="photo" role="img" aria-label="Fleet of racing sailboats at sea" style="left:0;top:0;width:374px;height:134px"></div>
  <div class="heading" style="left:0;top:141px;width:100%;text-align:center;font-size:10.5px">HEADING <span>GOES HERE</span></div>
  <div class="body" style="left:20px;top:156px;width:334px;text-align:center;font-size:3.8px">Lorem ipsum dolor sit amet, consectetur adipiscing elit. Vivamus eu dui ex. Curabitur dapibus dignissim dui, in molestie metus feugiat sed. Praesent aliquet lorem ex, eu dapibus odio varius at. Duis eget tellus porta, consequat lacus vitae, venenatis dolor. Nulla facilisi. In et sollicitudin lacus. Donec risus orci, gravida sit amet risus vehicula, aliquet pretium sapien. Nullam sit amet magna non ex bibendum mollis. Nunc vel neque eu augue dignissim congue ut vitae magna.</div>
  <div class="brand foot"><i class="dot"></i>TIMREL</div>
  <div class="pg">4</div>
</div>

<div class="slide" style="left:413px;top:963px">
  <div class="bracket tl sky" style="left:10px;top:10px"></div>
  <div class="heading" style="left:19px;top:36px">HEADING<br>GOES HERE</div>
  <div class="body" style="left:19px;top:66px;width:112px">Lorem ipsum dolor sit amet, consectetur adipiscing elit. Vivamus eu dui ex. Curabitur dapibus dignissim dui, in molestie metus feugiat sed. Praesent aliquet lorem ex, eu dapibus odio varius at. Duis eget tellus porta, consequat lacus vitae, venenatis dolor. Nulla facilisi. In et sollicitudin lacus. Donec risus orci, gravida sit amet risus vehicula, aliquet pretium sapien. Nullam sit amet magna non ex bibendum mollis. Nunc vel neque eu augue dignissim congue ut vitae magna. Phasellus eget commodo arcu.</div>
  <div class="photo" role="img" aria-label="Sailboats racing near a coastline" style="left:140px;top:0;width:234px;height:186px"></div>
  <div class="brand foot"><i class="dot"></i>TIMREL</div>
  <div class="pg">5</div>
</div>

<div class="slide" style="left:806px;top:963px">
  <div class="photo tint" role="img" aria-label="Sails against the sky in deep blue tint" style="left:0;top:0;width:374px;height:105px"></div>
  <div class="stitle" style="top:17px;color:#fff">OUR SERVICE</div>
  <svg class="icon" style="position:absolute;left:0;top:57px" width="374" height="40" viewBox="0 0 374 40">
    <g fill="var(--navy)" stroke="#fff" stroke-width="1.5">
      <circle cx="82" cy="20" r="16"/><circle cx="187" cy="20" r="16"/><circle cx="292" cy="20" r="16"/>
    </g>
    <g fill="#fff">
      <circle cx="77" cy="16" r="2.5"/><circle cx="87" cy="16" r="2.5"/><circle cx="82" cy="14" r="3"/>
      <path d="M71 26q6-7 11-5q5-2 11 5z"/>
      <path d="M187 9l0 15l-8 0z"/><path d="M189 12l6 12l-6 0z"/><path d="M178 26h18l-3 4h-12z"/>
      <path d="M292 10a6 6 0 0 1 6 6c0 5-6 12-6 12s-6-7-6-12a6 6 0 0 1 6-6z"/>
    </g>
    <circle cx="292" cy="16" r="2" fill="var(--navy)"/>
  </svg>
  <div class="heading" style="left:20px;top:117px;width:125px;text-align:center;font-size:5.5px">HEADING GOES HERE</div>
  <div class="heading" style="left:125px;top:117px;width:125px;text-align:center;font-size:5.5px">HEADING GOES HERE</div>
  <div class="heading" style="left:230px;top:117px;width:125px;text-align:center;font-size:5.5px">HEADING GOES HERE</div>
  <div class="body" style="left:42px;top:127px;width:80px;text-align:center;font-size:3.8px">Lorem ipsum dolor sit amet, consectetur adipiscing elit. Vivamus eu dui ex. Curabitur dapibus dignissim dui, in molestie metus feugiat sed. Praesent aliquet lorem ex, eget tellus porta, consequat lacus vitae, venenatis dolor.</div>
  <div class="body" style="left:147px;top:127px;width:80px;text-align:center;font-size:3.8px">Lorem ipsum dolor sit amet, consectetur adipiscing elit. Vivamus eu dui ex. Curabitur dapibus dignissim dui, in molestie metus feugiat sed. Praesent aliquet lorem ex, eget tellus porta, consequat lacus vitae, venenatis dolor.</div>
  <div class="body" style="left:252px;top:127px;width:80px;text-align:center;font-size:3.8px">Lorem ipsum dolor sit amet, consectetur adipiscing elit. Vivamus eu dui ex. Curabitur dapibus dignissim dui, in molestie metus feugiat sed. Praesent aliquet lorem ex, eget tellus porta, consequat lacus vitae, venenatis dolor.</div>
  <div class="brand foot"><i class="dot"></i>TIMREL</div>
  <div class="pg">6</div>
</div>

<!-- Row 3 -->
<div class="slide" style="left:20px;top:1192px">
  <div class="bracket tl sky" style="left:10px;top:10px"></div>
  <div class="heading" style="left:19px;top:36px">HEADING<br>GOES HERE</div>
  <div class="body" style="left:19px;top:66px;width:112px">Lorem ipsum dolor sit amet, consectetur adipiscing elit. Vivamus eu dui ex. Curabitur dapibus dignissim dui, in molestie metus feugiat sed. Praesent aliquet lorem ex, eu dapibus odio varius at. Duis eget tellus porta, consequat lacus vitae, venenatis dolor. Nulla facilisi. In et sollicitudin lacus. Donec risus orci, gravida sit amet risus vehicula, aliquet pretium sapien. Nullam sit amet magna non ex bibendum mollis. Nunc vel neque eu augue dignissim congue ut vitae magna. Phasellus eget commodo arcu.</div>
  <div class="photo fleet" role="img" aria-label="Large fleet of sailboats in grey light" style="left:140px;top:0;width:75px;height:186px"></div>
  <div class="photo crew" role="img" aria-label="Sailor trimming lines on deck" style="left:219px;top:0;width:75px;height:186px"></div>
  <div class="photo" role="img" aria-label="Yacht sailing past a headland" style="left:298px;top:0;width:76px;height:186px"></div>
  <div class="brand foot"><i class="dot"></i>TIMREL</div>
  <div class="pg">7</div>
</div>

<div class="slide" style="left:413px;top:1192px">
  <div class="stitle" style="top:17px">COMPANY PRESENTATION</div>
  <div class="card" style="left:40px;top:52px;width:88px;height:124px"><div class="photo green" role="img" aria-label="Racing yacht heeling through spray"></div><p style="font-weight:600;padding-top:5px">PROJECTS<br>Title Goes Here</p><p>Lorem ipsum dolor sit amet, consectetur adipiscing elit. Vivamus eu dui ex. Curabitur dapibus dignissim dui.</p></div>
  <div class="card" style="left:143px;top:52px;width:88px;height:124px"><div class="photo race" role="img" aria-label="Foiling catamarans lined up at a race start"></div><p style="font-weight:600;padding-top:5px">PROJECTS<br>Title Goes Here</p><p>Lorem ipsum dolor sit amet, consectetur adipiscing elit. Vivamus eu dui ex. Curabitur dapibus dignissim dui.</p></div>
  <div class="card" style="left:247px;top:52px;width:88px;height:124px"><div class="photo" role="img" aria-label="Sailboats on blue sea"></div><p style="font-weight:600;padding-top:5px">PROJECTS<br>Title Goes Here</p><p>Lorem ipsum dolor sit amet, consectetur adipiscing elit. Vivamus eu dui ex. Curabitur dapibus dignissim dui.</p></div>
  <div class="brand foot"><i class="dot"></i>TIMREL</div>
  <div class="pg">8</div>
</div>

<div class="slide" style="left:806px;top:1192px">
  <div style="position:absolute;left:0;top:0;width:374px;height:80px;background:var(--navy)"></div>
  <div class="heading" style="left:17px;top:11px;color:#fff;font-size:11px">LOREM IPSUM<br>DOLOR SIT AMET,<br>CONSECTETUR</div>
  <div class="body" style="left:17px;top:55px;color:#fff;font-size:4.3px">Lorem ipsum dolor sit amet, consectetur</div>
  <div class="body" style="left:17px;top:94px;width:140px">Lorem ipsum dolor sit amet, consectetur adipiscing elit. Vivamus eu dui ex. Curabitur dapibus dignissim dui, in molestie metus feugiat sed. Praesent aliquet lorem ex, eu dapibus odio varius at. Duis eget tellus porta, consequat lacus vitae, venenatis dolor. Nulla facilisi. In et sollicitudin lacus. Donec risus orci, gravida sit amet risus vehicula, aliquet pretium sapien. Nullam sit amet magna non ex bibendum mollis. Nunc vel neque eu augue dignissim congue ut vitae magna. Phasellus eget commodo arcu.</div>
  <div class="photo bluetint" role="img" aria-label="Sailboats in blue tint" style="left:167px;top:0;width:182px;height:171px"></div>
  <svg class="icon" style="position:absolute;left:175px;top:6px" width="30" height="160" viewBox="0 0 30 160">
    <g fill="#fff" stroke="var(--navy)" stroke-width="1.5"><circle cx="14" cy="20" r="11"/><circle cx="14" cy="59" r="11"/><circle cx="14" cy="98" r="11"/><circle cx="14" cy="137" r="11"/></g>
    <g fill="var(--navy)"><circle cx="14" cy="18" r="4"/><rect x="12" y="22" width="4" height="4"/>
      <path d="M14 92l0 8l-5 0z"/><path d="M15 94l4 6l-4 0z"/><rect x="8" y="101" width="12" height="1.5"/>
      <circle cx="14" cy="137" r="5"/></g>
    <g fill="none" stroke="var(--navy)" stroke-width="1.3"><circle cx="14" cy="59" r="5.5"/><path d="M14 55.5v4h3"/></g>
    <text x="14" y="139.5" fill="#fff" font-size="7" font-weight="700" text-anchor="middle" font-family="Work Sans,sans-serif">$</text>
  </svg>
  <div class="body" style="left:210px;top:12px;width:136px;color:#fff;font-size:3.9px;line-height:1.25"><b style="font-size:4.6px;font-weight:500;color:#dfe9ff">HEADING GOES HERE</b><br>Lorem ipsum dolor sit amet, consectetur adipiscing elit. Vivamus eu dui ex. Curabitur dapibus dignissim dui.</div>
  <div class="body" style="left:210px;top:51px;width:136px;color:#fff;font-size:3.9px;line-height:1.25"><b style="font-size:4.6px;font-weight:500;color:#dfe9ff">HEADING GOES HERE</b><br>Lorem ipsum dolor sit amet, consectetur adipiscing elit. Vivamus eu dui ex. Curabitur dapibus dignissim dui.</div>
  <div class="body" style="left:210px;top:90px;width:136px;color:#fff;font-size:3.9px;line-height:1.25"><b style="font-size:4.6px;font-weight:500;color:#dfe9ff">HEADING GOES HERE</b><br>Lorem ipsum dolor sit amet, consectetur adipiscing elit. Vivamus eu dui ex. Curabitur dapibus dignissim dui.</div>
  <div class="body" style="left:210px;top:129px;width:136px;color:#fff;font-size:3.9px;line-height:1.25"><b style="font-size:4.6px;font-weight:500;color:#dfe9ff">HEADING GOES HERE</b><br>Lorem ipsum dolor sit amet, consectetur adipiscing elit. Vivamus eu dui ex. Curabitur dapibus dignissim dui.</div>
  <div class="brand foot"><i class="dot"></i>TIMREL</div>
  <div class="pg">9</div>
</div>

<!-- Row 4 -->
<div class="slide" style="left:20px;top:1421px">
  <div class="bracket tl sky" style="left:10px;top:10px"></div>
  <div class="heading" style="left:19px;top:36px">HEADING<br>GOES HERE</div>
  <div class="body" style="left:19px;top:66px;width:112px">Lorem ipsum dolor sit amet, consectetur adipiscing elit. Vivamus eu dui ex. Curabitur dapibus dignissim dui, in molestie metus feugiat sed. Praesent aliquet lorem ex, eu dapibus odio varius at. Duis eget tellus porta, consequat lacus vitae, venenatis dolor. Nulla facilisi. In et sollicitudin lacus. Donec risus orci, gravida sit amet risus vehicula, aliquet pretium sapien. Nullam sit amet magna non ex bibendum mollis. Nunc vel neque eu augue dignissim congue ut vitae magna. Phasellus eget commodo arcu.</div>
  <div class="photo fleet" role="img" aria-label="Fleet of sailboats in grey light" style="left:140px;top:0;width:75px;height:92px"></div>
  <div class="photo green" role="img" aria-label="Racing yacht with green hull through waves" style="left:140px;top:96px;width:75px;height:90px"></div>
  <div class="photo race" role="img" aria-label="Foiling catamarans with colourful sails" style="left:219px;top:0;width:75px;height:186px"></div>
  <div class="photo" role="img" aria-label="Yachts near a coastline" style="left:298px;top:0;width:76px;height:92px"></div>
  <div class="photo crew" role="img" aria-label="Sailor working on deck" style="left:298px;top:96px;width:76px;height:90px"></div>
  <div class="brand foot"><i class="dot"></i>TIMREL</div>
  <div class="pg">10</div>
</div>

<div class="slide" style="left:413px;top:1421px">
  <div class="photo race" role="img" aria-label="Foiling catamarans racing with city skyline behind" style="left:0;top:0;width:235px;height:180px"></div>
  <div class="bracket tr sky" style="left:350px;top:10px"></div>
  <div class="heading" style="left:248px;top:36px">HEADING<br>GOES HERE</div>
  <div class="body" style="left:248px;top:66px;width:112px">Lorem ipsum dolor sit amet, consectetur adipiscing elit. Vivamus eu dui ex. Curabitur dapibus dignissim dui, in molestie metus feugiat sed. Praesent aliquet lorem ex, eu dapibus odio varius at. Duis eget tellus porta, consequat lacus vitae, venenatis dolor. Nulla facilisi. In et sollicitudin lacus. Donec risus orci, gravida sit amet risus vehicula, aliquet pretium sapien. Nullam sit amet magna non ex bibendum mollis. Nunc vel neque eu augue dignissim congue ut vitae magna. Phasellus eget commodo arcu.</div>
  <div class="brand foot"><i class="dot"></i>TIMREL</div>
  <div class="pg">11</div>
</div>

<div class="slide" style="left:806px;top:1421px">
  <div class="photo race" role="img" aria-label="Racing yacht sails against cloudy sky" style="left:0;top:0;width:235px;height:92px"></div>
  <div class="photo foil" role="img" aria-label="Trimaran racing over dark water" style="left:0;top:92px;width:235px;height:88px"></div>
  <div class="bracket tr sky" style="left:350px;top:10px"></div>
  <div class="heading" style="left:248px;top:36px">HEADING<br>GOES HERE</div>
  <div class="body" style="left:248px;top:66px;width:112px">Lorem ipsum dolor sit amet, consectetur adipiscing elit. Vivamus eu dui ex. Curabitur dapibus dignissim dui, in molestie metus feugiat sed. Praesent aliquet lorem ex, eu dapibus odio varius at. Duis eget tellus porta, consequat lacus vitae, venenatis dolor. Nulla facilisi. In et sollicitudin lacus. Donec risus orci, gravida sit amet risus vehicula, aliquet pretium sapien. Nullam sit amet magna non ex bibendum mollis. Nunc vel neque eu augue dignissim congue ut vitae magna. Phasellus eget commodo arcu.</div>
  <div class="brand foot"><i class="dot"></i>TIMREL</div>
  <div class="pg">12</div>
</div>

<!-- Row 5 -->
<div class="slide" style="left:20px;top:1650px">
  <div class="photo" role="img" aria-label="Sailboats on blue sea" style="left:0;top:0;width:115px;height:88px"></div>
  <div class="photo race" role="img" aria-label="Racing yacht sails against clouds" style="left:119px;top:0;width:116px;height:88px"></div>
  <div class="photo foil" role="img" aria-label="Trimaran at speed" style="left:0;top:92px;width:115px;height:88px"></div>
  <div class="photo green" role="img" aria-label="Green-hulled yacht heeling" style="left:119px;top:92px;width:116px;height:88px"></div>
  <div class="bracket tr sky" style="left:350px;top:10px"></div>
  <div class="heading" style="left:248px;top:36px">HEADING<br>GOES HERE</div>
  <div class="body" style="left:248px;top:66px;width:112px">Lorem ipsum dolor sit amet, consectetur adipiscing elit. Vivamus eu dui ex. Curabitur dapibus dignissim dui, in molestie metus feugiat sed. Praesent aliquet lorem ex, eu dapibus odio varius at. Duis eget tellus porta, consequat lacus vitae, venenatis dolor. Nulla facilisi. In et sollicitudin lacus. Donec risus orci, gravida sit amet risus vehicula, aliquet pretium sapien. Nullam sit amet magna non ex bibendum mollis. Phasellus eget commodo arcu.</div>
  <div class="brand foot"><i class="dot"></i>TIMREL</div>
  <div class="pg">13</div>
</div>

<div class="slide" style="left:413px;top:1650px">
  <div class="stitle" style="top:17px">TIMELINE SLIDE</div>
  <svg style="position:absolute;left:0;top:0" width="374" height="211" viewBox="0 0 374 211" font-family="Work Sans,sans-serif">
    <rect x="28" y="109" width="346" height="6" fill="#e6e8ee"/>
    <g stroke="var(--sky)" stroke-width=".6"><line x1="29" y1="104" x2="29" y2="170"/><line x1="138" y1="104" x2="138" y2="170"/><line x1="248" y1="104" x2="248" y2="170"/></g>
    <g stroke="var(--navy)" stroke-width=".6"><line x1="86" y1="70" x2="86" y2="125"/><line x1="195" y1="70" x2="195" y2="125"/></g>
    <g fill="var(--navy)"><circle cx="86" cy="125" r="1.3"/><circle cx="195" cy="125" r="1.3"/></g>
    <g font-size="4.3" fill="var(--sky)" text-anchor="middle"><text x="29" y="101">2008</text><text x="138" y="101">2016</text><text x="248" y="101">2022</text></g>
    <g font-size="4.3" fill="var(--navy)" font-weight="600" text-anchor="middle"><text x="86" y="132">2010</text><text x="195" y="132">2018</text></g>
    <g font-size="4.3" fill="var(--navy)" font-weight="600"><text x="90" y="61">Lorem ipsum dolor sit</text><text x="199" y="61">Lorem ipsum dolor sit</text></g>
    <g font-size="3" fill="#555"><text x="90" y="66">Lorem ipsum dolor sit amet,</text><text x="90" y="70">consectetur adipiscing elit, sed do</text><text x="90" y="74">eiusmod tempor incididunt labore.</text>
      <text x="199" y="66">Lorem ipsum dolor sit amet,</text><text x="199" y="70">consectetur adipiscing elit, sed do</text><text x="199" y="74">eiusmod tempor incididunt labore.</text></g>
    <g font-size="4.3" fill="var(--sky)"><text x="33" y="156">Lorem ipsum dolor sit</text><text x="142" y="156">Lorem ipsum dolor sit</text><text x="252" y="156">Lorem ipsum dolor sit</text></g>
    <g font-size="3" fill="#555"><text x="33" y="161">Lorem ipsum dolor sit amet,</text><text x="33" y="165">consectetur adipiscing elit, sed do</text><text x="33" y="169">eiusmod tempor incididunt labore.</text>
      <text x="142" y="161">Lorem ipsum dolor sit amet,</text><text x="142" y="165">consectetur adipiscing elit, sed do</text><text x="142" y="169">eiusmod tempor incididunt labore.</text>
      <text x="252" y="161">Lorem ipsum dolor sit amet,</text><text x="252" y="165">consectetur adipiscing elit, sed do</text><text x="252" y="169">eiusmod tempor incididunt labore.</text></g>
  </svg>
  <div class="brand foot"><i class="dot"></i>TIMREL</div>
  <div class="pg">14</div>
</div>

<div class="slide" style="left:806px;top:1650px">
  <div class="stitle" style="top:17px">TABLE SLIDE</div>
  <table style="position:absolute;left:15px;top:53px;width:344px;font-size:4px;text-align:center;color:#444">
    <tr style="background:var(--navy);color:#fff;height:14px"><td rowspan="2" style="text-align:left;padding-left:4px;font-size:7px;font-weight:500">HEADING GOES HERE</td><td style="background:var(--mid);font-size:7.5px">2020</td><td style="background:var(--blue);font-size:7.5px">2021</td><td style="background:var(--blue);font-size:7.5px">2022</td></tr>
    <tr style="height:9px"><td>(Lorem Ipsum)</td><td>(Lorem Ipsum)</td><td>(Lorem Ipsum)</td></tr>
    <tr style="height:11px;border-bottom:.5px solid #e3e6ee"><td style="text-align:left;color:var(--mid);padding-left:4px">Duis Eget Tellus Porta</td><td>67</td><td>77</td><td>23</td></tr>
    <tr style="height:11px;border-bottom:.5px solid #e3e6ee"><td style="text-align:left;color:var(--mid);padding-left:4px">Praesent Aliquet Lorem</td><td>12</td><td>64</td><td>88</td></tr>
    <tr style="height:11px;border-bottom:.5px solid #e3e6ee"><td style="text-align:left;color:var(--mid);padding-left:4px">Lorem Ipsum Dolor Sit Amet</td><td>90</td><td>34</td><td>98</td></tr>
    <tr style="height:11px;border-bottom:.5px solid #e3e6ee"><td style="text-align:left;color:var(--mid);padding-left:4px">Curabitur Dapibus Molestie</td><td>99</td><td>90</td><td>11</td></tr>
    <tr style="height:11px;border-bottom:.5px solid #e3e6ee"><td style="text-align:left;color:var(--mid);padding-left:4px">Vivamus Eu Dui Ex</td><td>34</td><td>23</td><td>23</td></tr>
    <tr style="height:11px;border-bottom:.5px solid #e3e6ee"><td style="text-align:left;color:var(--mid);padding-left:4px">Lorem Ipsum Dolor Amet</td><td>56</td><td>44</td><td>45</td></tr>
    <tr style="height:11px"><td style="text-align:left;color:var(--mid);padding-left:4px">Duis Eget Tellus Porta</td><td>12</td><td>67</td><td>78</td></tr>
    <tr style="height:13px;color:#fff;font-size:6px;font-weight:600"><td style="background:var(--deep)"></td><td style="background:var(--mid)">800</td><td style="background:var(--blue)">900</td><td style="background:var(--blue)">1000</td></tr>
  </table>
  <div class="brand foot"><i class="dot"></i>TIMREL</div>
  <div class="pg">15</div>
</div>

<!-- Row 6 -->
<div class="slide" style="left:20px;top:1880px">
  <div class="stitle" style="top:17px">CHART SLIDE</div>
  <svg style="position:absolute;left:0;top:0" width="374" height="211" viewBox="0 0 374 211" font-family="Work Sans,sans-serif">
    <ellipse cx="187" cy="114" rx="68" ry="38" fill="var(--deep)"/>
    <path d="M187 107 L187 69 A68 38 0 0 1 253 98 Z" fill="var(--sky)"/>
    <path d="M187 107 L253 98 A68 38 0 0 1 170 144 Z" fill="var(--mid)"/>
    <path d="M187 107 L170 144 A68 38 0 0 1 122 96 Z" fill="var(--blue)"/>
    <path d="M187 107 L122 96 A68 38 0 0 1 187 69 Z" fill="var(--navy)"/>
    <g font-size="4.5" fill="#fff" text-anchor="middle"><text x="155" y="83">25%</text><text x="218" y="83">20%</text><text x="225" y="125">36%</text><text x="136" y="113">12%</text></g>
    <g font-size="15" fill="var(--mid)" text-anchor="middle"><text x="68" y="78">25%</text><text x="68" y="146">12%</text><text x="307" y="78">20%</text><text x="307" y="146">36%</text></g>
    <g font-size="5" fill="var(--mid)" font-weight="600" text-anchor="middle"><text x="68" y="86">LOREM IPSUM DOLOR</text><text x="68" y="154">LOREM IPSUM DOLOR</text><text x="307" y="86">LOREM IPSUM DOLOR</text><text x="307" y="154">LOREM IPSUM DOLOR</text></g>
    <g font-size="3.4" fill="#555" text-anchor="middle">
      <text x="68" y="92">Nunc placerat, arcu nec mattis</text><text x="68" y="96">fermentum, nisi mauris convallis</text><text x="68" y="100">nunc, ut luctus nunc nisl id ex.</text>
      <text x="68" y="160">Nunc placerat, arcu nec mattis</text><text x="68" y="164">fermentum, nisi mauris convallis</text><text x="68" y="168">nunc, ut luctus nunc nisl id ex.</text>
      <text x="307" y="92">Nunc placerat, arcu nec mattis</text><text x="307" y="96">fermentum, nisi mauris convallis</text><text x="307" y="100">nunc, ut luctus nunc nisl id ex.</text>
      <text x="307" y="160">Nunc placerat, arcu nec mattis</text><text x="307" y="164">fermentum, nisi mauris convallis</text><text x="307" y="168">nunc, ut luctus nunc nisl id ex.</text></g>
  </svg>
  <div class="brand foot"><i class="dot"></i>TIMREL</div>
  <div class="pg">16</div>
</div>

<div class="slide" style="left:413px;top:1880px">
  <div class="stitle" style="top:17px">CHART SLIDE</div>
  <svg style="position:absolute;left:0;top:0" width="374" height="211" viewBox="0 0 374 211" font-family="Work Sans,sans-serif">
    <g font-size="3.3" fill="#555" text-anchor="end"><text x="20" y="57">6</text><text x="20" y="73">5</text><text x="20" y="89">4</text><text x="20" y="105">3</text><text x="20" y="121">2</text><text x="20" y="137">1</text><text x="20" y="153">0</text></g>
    <line x1="24" y1="152" x2="190" y2="152" stroke="#ccc" stroke-width=".5"/>
    <g fill="var(--sky)"><rect x="33" y="82" width="6" height="70"/><rect x="73" y="117" width="6" height="35"/><rect x="113" y="96" width="6" height="56"/><rect x="153" y="82" width="6" height="70"/></g>
    <g fill="var(--mid)"><rect x="40" y="114" width="6" height="38"/><rect x="80" y="76" width="6" height="76"/><rect x="120" y="117" width="6" height="35"/><rect x="160" y="96" width="6" height="56"/></g>
    <g fill="var(--navy)"><rect x="47" y="120" width="6" height="32"/><rect x="87" y="120" width="6" height="32"/><rect x="127" y="104" width="6" height="48"/><rect x="167" y="72" width="6" height="80"/></g>
    <g font-size="3.3" fill="#555" text-anchor="middle"><text x="43" y="158">Category 1</text><text x="83" y="158">Category 2</text><text x="123" y="158">Category 3</text><text x="163" y="158">Category 4</text></g>
    <g font-size="3.4" fill="#555"><text x="18" y="170">Lorem ipsum dolor sit amet, consectetur adipiscing elit. Vivamus eu dui</text><text x="18" y="174">ex. Curabitur dapibus dignissim dui, in molestie metus feugiat sed.</text><text x="18" y="178">Praesent aliquet lorem ex.</text></g>
    <g fill="#fff" stroke="#c9d6f2" stroke-width=".7"><rect x="204" y="48" width="156" height="38" rx="2"/><rect x="204" y="92" width="156" height="38" rx="2"/><rect x="204" y="136" width="156" height="38" rx="2"/></g>
    <g font-size="14" fill="var(--mid)" text-anchor="middle"><text x="282" y="68">160,000</text><text x="282" y="112">13,000</text><text x="282" y="156">150</text></g>
    <g font-size="3.4" fill="#555" text-anchor="middle"><text x="282" y="78">Lorem ipsum dolor sit amet, consectetur adipiscing elit.</text><text x="282" y="122">Lorem ipsum dolor sit amet, consectetur adipiscing elit.</text><text x="282" y="166">Lorem ipsum dolor sit amet, consectetur adipiscing elit.</text></g>
  </svg>
  <div class="brand foot"><i class="dot"></i>TIMREL</div>
  <div class="pg">17</div>
</div>

<div class="slide" style="left:806px;top:1880px">
  <div style="position:absolute;left:0;top:0;width:133px;height:211px;background:var(--navy)"></div>
  <div class="bracket tl sky" style="left:10px;top:10px"></div>
  <div class="heading" style="left:19px;top:32px;color:#fff;font-size:11px">LOCATION<br>SLIDE</div>
  <div style="position:absolute;left:17px;top:72px;width:110px;font-size:3.8px;color:#fff">
    <div style="border:.6px solid var(--sky);border-radius:2px;padding:3px 4px;margin-bottom:5px">1. Duis Eget Tellus Porta</div>
    <div style="border:.6px solid var(--sky);border-radius:2px;padding:3px 4px;margin-bottom:5px">2. sed do eiusmod tempor incididunt</div>
    <div style="border:.6px solid var(--sky);border-radius:2px;padding:3px 4px;margin-bottom:5px">3. Duis Eget Tellus Porta</div>
    <div style="border:.6px solid var(--sky);border-radius:2px;padding:3px 4px;margin-bottom:5px">4. sed do eiusmod tempor incididunt</div>
    <div style="border:.6px solid var(--sky);border-radius:2px;padding:3px 4px;margin-bottom:5px">5. Duis Eget Tellus Porta</div>
    <div style="border:.6px solid var(--sky);border-radius:2px;padding:3px 4px">6. sed do eiusmod tempor incididunt</div>
  </div>
  <div class="photo map" role="img" aria-label="World map in grey with highlighted countries in navy" style="left:140px;top:40px;width:228px;height:130px"></div>
  <div class="brand foot light"><i class="dot"></i>TIMREL</div>
  <div class="pg">18</div>
</div>

<!-- Row 7 -->
<div class="slide" style="left:216px;top:2119px">
  <div style="position:absolute;left:0;top:0;width:374px;height:125px;background:var(--navy)"></div>
  <div class="heading" style="left:19px;top:40px;color:#fff;font-size:11px">COMPARAISON<br>SLIDE</div>
  <div class="body" style="left:19px;top:72px;width:100px;color:#fff;font-size:4.5px">Lorem ipsum dolor sit amet, consectetur adipiscing elit. Vivamus eu dui ex. Curabitur dapibus dignissim dui.</div>
  <div class="body" style="left:19px;top:138px;width:100px;font-size:3.8px">Lorem ipsum dolor sit amet, consectetur adipiscing elit. Vivamus eu dui ex. Curabitur dapibus dignissim dui. Lorem ipsum dolor sit amet, consectetur adipiscing elit. Vivamus eu dui ex. Curabitur dapibus dignissim dui.</div>
  <svg style="position:absolute;left:0;top:0" width="374" height="211" viewBox="0 0 374 211" font-family="Work Sans,sans-serif">
    <g fill="#fff"><rect x="126" y="20" width="72" height="170" rx="36" ry="36"/><rect x="206" y="20" width="72" height="170" rx="36" ry="36"/><rect x="286" y="20" width="72" height="170" rx="36" ry="36"/>
      <rect x="126" y="150" width="72" height="40"/><rect x="206" y="150" width="72" height="40"/><rect x="286" y="150" width="72" height="40"/></g>
    <g fill="var(--navy)"><circle cx="162" cy="56" r="30"/><circle cx="242" cy="56" r="30"/><circle cx="322" cy="56" r="30"/></g>
    <g font-size="17" fill="#fff" text-anchor="middle"><text x="162" y="62">1</text><text x="242" y="62">2</text><text x="322" y="62">3</text></g>
    <g font-size="6.5" text-anchor="middle" font-weight="600"><text x="162" y="99" fill="var(--sky)">TITLE</text><text x="162" y="107" fill="var(--sky)">GOES HERE</text><text x="242" y="99" fill="var(--navy)">TITLE</text><text x="242" y="107" fill="var(--navy)">GOES HERE</text><text x="322" y="99" fill="var(--sky)">TITLE</text><text x="322" y="107" fill="var(--sky)">GOES HERE</text></g>
    <g font-size="3.5" fill="#555" text-anchor="middle"><text x="162" y="114">Lorem ipsum dolor</text><text x="242" y="114">Lorem ipsum dolor</text><text x="322" y="114">Lorem ipsum dolor</text></g>
    <g font-size="3.3" fill="#555">
      <text x="134" y="126">• Lorem ipsum dolor sit.</text><text x="134" y="132">• Consectetur adipiscing.</text><text x="134" y="138">• Vivamus eu dui ex.</text><text x="134" y="144">• Curabitur dapibus.</text><text x="134" y="150">• Lorem ipsum dolor sit.</text><text x="134" y="156">• Curabitur dapibus.</text>
      <text x="214" y="126">• Lorem ipsum dolor sit.</text><text x="214" y="132">• Consectetur adipiscing.</text><text x="214" y="138">• Vivamus eu dui ex.</text><text x="214" y="144">• Curabitur dapibus.</text><text x="214" y="150">• Lorem ipsum dolor sit.</text><text x="214" y="156">• Curabitur dapibus.</text>
      <text x="294" y="126">• Lorem ipsum dolor sit.</text><text x="294" y="132">• Consectetur adipiscing.</text><text x="294" y="138">• Vivamus eu dui ex.</text><text x="294" y="144">• Curabitur dapibus.</text><text x="294" y="150">• Lorem ipsum dolor sit.</text><text x="294" y="156">• Curabitur dapibus.</text></g>
    <rect x="132" y="168" width="60" height="9" fill="var(--sky)"/><rect x="212" y="168" width="60" height="9" fill="var(--navy)"/><rect x="292" y="168" width="60" height="9" fill="var(--deep)"/>
    <g font-size="3.6" fill="#fff" text-anchor="middle"><text x="162" y="174">Text Goes Here</text><text x="242" y="174">Text Goes Here</text><text x="322" y="174">Text Goes Here</text></g>
  </svg>
  <div class="brand foot"><i class="dot"></i>TIMREL</div>
  <div class="pg">19</div>
</div>

<div class="slide" style="left:609px;top:2119px">
  <div class="photo fleet" role="img" aria-label="Large fleet of sailboats on grey water" style="left:0;top:0;width:374px;height:165px"></div>
  <div class="band" style="top:165px;height:46px"></div>
  <div class="copy" style="left:22px;top:188px">Copyright © 2022 TIMREL. All rights reserved.</div>
  <div class="bracket tl" style="left:142px;top:28px"></div>
  <div class="titlebox" style="left:167px;top:0;width:155px;height:183px;justify-content:flex-start;padding-top:22px">
    <div class="brand light" style="position:static;font-size:12px"><i class="dot" style="width:8px;height:8px"></i>TIMREL</div>
    <h1 style="font-size:14px;margin-top:14px">THANK YOU!</h1>
    <p style="font-size:4.5px">For Your Time And Attention</p>
    <p style="font-size:6px;margin-top:16px;font-weight:500">CONTACT US</p>
    <svg width="120" height="48" viewBox="0 0 120 48" style="margin-top:4px" font-family="Work Sans,sans-serif">
      <g fill="none" stroke="var(--sky)" stroke-width=".6"><rect x="26" y="2" width="92" height="10" rx="5"/><rect x="26" y="17" width="92" height="10" rx="5"/><rect x="26" y="32" width="92" height="10" rx="5"/></g>
      <g fill="#fff">
        <path d="M7 3q-2 1-1 4t5 5q3 1 4-1l-2-2-1 1q-2-1-3-3l1-1z"/>
        <rect x="5" y="19" width="9" height="6" rx="1"/>
        <circle cx="9.5" cy="37" r="4.5"/>
      </g>
      <path d="M5 19l4.5 3.5l4.5-3.5" fill="none" stroke="var(--navy)" stroke-width=".8"/>
      <g fill="none" stroke="var(--navy)" stroke-width=".6"><ellipse cx="9.5" cy="37" rx="2" ry="4.5"/><line x1="5" y1="37" x2="14" y2="37"/></g>
      <g font-size="4" fill="#fff"><text x="34" y="8.5">Insert Phone Number</text><text x="34" y="23.5">Insert E-Mail Address</text><text x="34" y="38.5">Insert URL Address</text></g>
    </svg>
  </div>
  <div class="bracket br" style="left:322px;top:183px"></div>
</div>

</body>
</html>
```